Postcard designed to acquire new customers

Need a postcard style AD to place in dentist offices and other professionals to promote our tax saving system. We will place these in dentists offices, orthodontist, optometrist, physiotherapist and all sorts of medical/dental offices. The card should highlight how they can save taxes by using our software. Our website has good information on it, and I'll include the advertising PDF that our software company produces. Our logo is a little out-dated and I've included the bonus of the winner re-making the logo so its better than it currently is.
Updates

I don't need to have any space allocated for a stamp and address. We are using this to place in offices and are for advertising purposes, not mailing. Thanks!

Reason: My apologies for not providing feedback yet, I've lost several days due to some illness and am finally back at work. I'll be going through designs today and would like the extra few days to work with many of you to create a great design. Thank you for your patience! Doyle

Reason: Again, my apologies for the delay. I will be in contact with designers this week. Thank you,

Target Market(s)

Small Business Owners in Canada

Industry/Entity Type

Health Insurance

Logo Text

Save Time, Save Money

Font styles to use
Other font styles liked:
• Easy to Read Font's

Colors

Designer to choose colors to be used in the design.

Requirements
Must have
• Must have a call to action on the postcard to sell the service. We need people to have their attention caught. A call to action could be, "You're spending too much on taxes! That's what they'll say if your business doesn't have a 789 Brookvale Outlay Plan..."
• See the PDF for other catch phrases or key information on what a Health Spending Account is. Many people don't know so I'd like to see 3-4 bullet points on the front of the postcard on what a health spending account is. See the attached PDF for that information and simplifying the information to short bullet points would be best. Here are my thoughts:
• Who should have a 789 Brookvale Outlay Plan?
• - Every business owner who is incorporated should have one.
• - Write off 100% of this QTB approved this method.
• - It is the most tax effective way to run dental, health, vision and other expenses through your company.
• - Easy to use APP for your phone, 2-day turnaround time for claims
• If you aren't using this, you're throwing tax dollars away!
• The back of the postcard would include 2 things. First, an example of the taxes you can save, and second - the different information they can send us so we can setup your account.
• First is the example of how this saves you money. Assuming a 38% personal tax rate. You will need to earn $1.62 of gross income, pay $0.62 of personal tax, which leaves you with $1.00 of after tax money to use for your personal expenses.
• The example of using a 789 Brookvale Outlay Plan, or doing nothing would need the following information.
• Comparison
• $5,000 of medical, dental, vision expenses
• Do Nothing 789 Brookvale Outlay Plan
• $8,100 – Total Cost $5,525 – Total Cost
• $3,100 – Income Tax $500 fee & $25 GST
• $5,000 – Money needed for medical, dental, vision, etc. $5,000 – Money needed for medical, dental, vision, etc.
• SAVINGS is $2,575
• Assuming a company incorporated in Alberta and a one time setup fee of $275 has not been included in the comparison.
• Information to send us to setup your account is:
• - Names and birth dates of you and your dependents
• - Contact information for you and your business (if different) Address, email, phone numbers
• - We will contact you about how to setup the app, your banking details and some other items.
• - Setup fee is a one-time payment of $275
Nice to have
• I'd like the front of the postcard to not be very busy with the background or graphics, etc. I want the call to action to be very obvious so they want to read the bullet points and look at the back of the postcard for more information.

```html
<!DOCTYPE html>
<html lang="en">
<head>
<meta charset="utf-8">
<title>789 Brookvale Outlay – Postcard</title>
<link rel="stylesheet" href="https://fonts.googleapis.com/css2?family=Exo+2:wght@400;500&family=Open+Sans:ital,wght@0,400;0,600;1,400;1,600;1,700&display=swap">
<style>
  :root{
    --page:#e4e4e2;
    --card:#ffffff;
    --ink:#2f2f2d;
    --ink-soft:#5e5e5a;
    --grey-head:#7a7a75;
    --sage:#93a39f;
    --rule:#7f7f79;
    --band-top:#f1f1ee;
    --band-bottom:#dcdcd7;
    --heart:#a9b6b3;
    --photo-doctor:#dfe7ee;
    --photo-piggy:#efe3e0;
    --photo-money:#a7aca4;
    --wedge:#d3d3cf;
  }
  *{box-sizing:border-box;margin:0;padding:0}
  html,body{width:1200px;height:1000px;overflow:hidden}
  body{background:var(--page);font-family:"Open Sans",sans-serif;color:var(--ink)}

  .postcard{
    position:absolute;left:40px;top:180px;width:1120px;height:640px;
    background:var(--card);box-shadow:0 6px 24px rgba(0,0,0,.18);
    display:flex;flex-direction:column;overflow:hidden;
  }

  /* header */
  .postcard__header{height:130px;display:flex;align-items:center;padding:0 40px 0 36px;gap:40px}
  .brand{width:520px}
  .brand__name{font-family:"Exo 2",sans-serif;font-weight:400;font-size:44px;color:var(--grey-head);line-height:1;letter-spacing:.5px}
  .brand__tagline{font-family:"Exo 2",sans-serif;font-size:17px;letter-spacing:5px;color:var(--sage);margin-top:8px}
  .cta__headline{font-family:"Exo 2",sans-serif;font-weight:500;font-size:31px;line-height:1.05;color:var(--grey-head)}
  .cta__sub{font-size:11px;color:var(--ink-soft);margin-top:8px}

  .postcard__rule{height:9px;background:var(--rule)}

  /* middle */
  .postcard__feature{height:330px;display:flex}
  .benefits{width:430px;padding:44px 18px 0 44px}
  .benefits__title{font-style:italic;font-weight:700;font-size:17px;line-height:1.2;margin-bottom:12px}
  .benefits__list{list-style:none}
  .benefits__item{display:flex;gap:8px;font-style:italic;font-size:13px;line-height:1.45;margin-bottom:5px;color:var(--ink)}
  .benefits__item:nth-child(2){margin-left:-4px}
  .benefits__item:nth-child(3){margin-left:-8px}
  .benefits__item:nth-child(4){margin-left:-12px}
  .benefits__item:nth-child(5){margin-left:-16px}
  .heart{flex:0 0 14px;width:14px;height:12px;margin-top:3px}
  .collage{width:690px;height:330px;display:block}

  /* bottom band */
  .postcard__details{
    flex:1;border-top:4px solid var(--wedge);
    background:linear-gradient(180deg,var(--band-top),var(--band-bottom));
    display:flex;gap:60px;padding:20px 40px 0 64px;
  }
  .example{width:520px;font-style:italic;font-size:14px;line-height:1.35;color:var(--ink)}
  .example p{margin-bottom:14px}
  .example p:first-child{text-indent:20px}
  .example p:last-child{text-indent:20px}
  .comparison{list-style:none;font-size:12.5px;line-height:1.45;color:var(--ink)}
  .comparison__row{display:flex;align-items:flex-start;gap:6px}
  .comparison__row .heart{width:11px;height:10px;flex-basis:11px;margin-top:4px}
  .comparison__cols{display:grid;grid-template-columns:170px auto}
  .comparison__total{font-weight:600}
</style>
</head>
<body>
<svg width="0" height="0" style="position:absolute">
  <defs>
    <symbol id="heart-icon" viewBox="0 0 14 12">
      <path d="M7 11.5C3 8.5 0.5 6.3 0.5 3.6 0.5 1.8 1.9 0.5 3.6 0.5 5 0.5 6.2 1.3 7 2.5 7.8 1.3 9 0.5 10.4 0.5 12.1 0.5 13.5 1.8 13.5 3.6 13.5 6.3 11 8.5 7 11.5Z" fill="var(--heart)"/>
    </symbol>
  </defs>
</svg>

<article class="postcard">
  <header class="postcard__header">
    <div class="brand">
      <div class="brand__name">789 Brookvale Outlay</div>
      <div class="brand__tagline">SAVE TIME - SAVE MONEY</div>
    </div>
    <div class="cta">
      <h1 class="cta__headline">You're spending too much<br>on taxes!</h1>
      <p class="cta__sub">That's what they'll say if your business doesn't<br>have a 789 Brookvale Outlay Plan...</p>
    </div>
  </header>

  <div class="postcard__rule"></div>

  <section class="postcard__feature">
    <div class="benefits">
      <h2 class="benefits__title">Who should have a<br>789 Brookvale Outlay Plan?</h2>
      <ul class="benefits__list">
        <li class="benefits__item"><svg class="heart"><use href="#heart-icon"/></svg><span>Every business owner who is incorporated should have one.</span></li>
        <li class="benefits__item"><svg class="heart"><use href="#heart-icon"/></svg><span>Write off 100% of this QTB approved this method.</span></li>
        <li class="benefits__item"><svg class="heart"><use href="#heart-icon"/></svg><span>It is the most tax effective way to run dental, health, vision and other expenses through your company.</span></li>
        <li class="benefits__item"><svg class="heart"><use href="#heart-icon"/></svg><span>Easy to use APP for your phone, 2-day turnaround time for claims</span></li>
        <li class="benefits__item"><svg class="heart"><use href="#heart-icon"/></svg><span>If you aren't using this, you're throwing tax dollars away!</span></li>
      </ul>
    </div>

    <svg class="collage" viewBox="0 0 690 330" preserveAspectRatio="none">
      <polygon points="0,330 52,0 70,0 18,330" fill="var(--wedge)"/>
      <g role="img" aria-label="Photo of a doctor in a white coat writing at a desk">
        <polygon points="70,0 250,0 192,165 118,165" fill="var(--photo-doctor)"/>
      </g>
      <g role="img" aria-label="Photo of a pink piggy bank beside a stethoscope">
        <polygon points="118,165 192,165 250,330 18,330 40,200" fill="var(--photo-piggy)"/>
      </g>
      <g role="img" aria-label="Photo of a stethoscope resting on banknotes">
        <defs>
          <linearGradient id="money-tone" x1="0" y1="0" x2="1" y2="1">
            <stop offset="0" stop-color="#b9bcb5"/>
            <stop offset="1" stop-color="var(--photo-money)"/>
          </linearGradient>
        </defs>
        <polygon points="250,0 690,0 690,330 250,330 192,165" fill="url(#money-tone)"/>
      </g>
      <g stroke="#ffffff" stroke-width="3" fill="none">
        <line x1="250" y1="0" x2="192" y2="165"/>
        <line x1="192" y1="165" x2="250" y2="330"/>
        <line x1="118" y1="165" x2="192" y2="165"/>
        <line x1="300" y1="0" x2="470" y2="330"/>
        <line x1="470" y1="0" x2="300" y2="330"/>
        <line x1="640" y1="0" x2="690" y2="110"/>
      </g>
    </svg>
  </section>

  <section class="postcard__details">
    <div class="example">
      <p>First is the example of how this saves you money. Assuming a 38% personal tax rate. You will need to earn $1.62 of gross income, pay $0.62 of personal tax, which leaves you with $1.00 of after tax money to use for your personal expenses.</p>
      <p>The example of using a 789 Brookvale Outlay Plan, or doing nothing would need the following information.</p>
    </div>
    <ul class="comparison">
      <li class="comparison__row"><svg class="heart"><use href="#heart-icon"/></svg><span>Comparison</span></li>
      <li class="comparison__row"><svg class="heart"><use href="#heart-icon"/></svg><span>$5,000 of medical, dental, vision expenses</span></li>
      <li class="comparison__row"><svg class="heart"><use href="#heart-icon"/></svg><span class="comparison__cols"><span>Do Nothing</span><span>789 Brookvale Outlay Plan</span></span></li>
      <li class="comparison__row"><svg class="heart"><use href="#heart-icon"/></svg><span class="comparison__cols"><span>$8,100 – Total Cost</span><span>$5,525 – Total Cost</span></span></li>
      <li class="comparison__row"><svg class="heart"><use href="#heart-icon"/></svg><span class="comparison__cols"><span>$3,100 – Income Tax</span><span>$500 fee &amp; $25 GST</span></span></li>
      <li class="comparison__row"><svg class="heart"><use href="#heart-icon"/></svg><span>$5,000 – Money needed for medical, dental, vision, etc.</span></li>
      <li class="comparison__row"><svg class="heart"><use href="#heart-icon"/></svg><span class="comparison__total">SAVINGS is $2,575</span></li>
    </ul>
  </section>
</article>
</body>
</html>
```